Steel Company / Iron Railing Business Card Template

We are a custom steel fabrication company located in Trainer, PA. In business since 1979, we recently developed a new logo, and we're looking for a business card design to help display the new logo and our business. The name of the company is Kelbrook Forge Co.. The Office Phone number is (610) 555-0143. We fabricate and install custom "wrought iron" railings on our residential side, we also fabricate and erect structural steel (think cranes and steel beams in buildings) on our commercial side. Looking to get a business card template designed. Something modern, but professional. Clear and easy to read. Front should have all business and employee information including phone number(s), email address, business information, etc. back should spotlight logo.

Industry/Entity Type

Construction / Home Improvement

Contact Information for Business Card

Business information is Kelbrook Forge Co., 48 Dunmore Ave Suite 3305, Trainer, PA 19074. Phone number is (610) 555-0143. Website is www.kelbrookforge.example Business card should be for "Tom Pelling" with the job title "Sales & Estimating" but be editable for other employees. Tom's phone number is (610) 555-0178

Colors

Designer to choose colors to be used in the design.

Requirements
Must have
• Modern Feel, Design should be sized for standard business card sizing 3.5" x 2" (88.9mm x 50.8mm)

```html
<!DOCTYPE html>
<html lang="en">
<head>
<meta charset="utf-8">
<title>Kelbrook Forge Co. — Business Card</title>
<link rel="stylesheet" href="https://fonts.googleapis.com/css2?family=Arimo:wght@400;700&family=Cinzel:wght@700&display=swap">
<style>
  :root {
    --backdrop: #5b5b5b;
    --brand-blue: #24418f;
    --brand-red: #d42229;
    --ink-grey: #464646;
    --rule-grey: #cfcfcf;
    --paper: #ffffff;
    --back-mark: #4a73cf;
  }
  * { margin: 0; padding: 0; box-sizing: border-box; }
  html, body { width: 1200px; height: 1200px; overflow: hidden; }
  body {
    background: var(--backdrop);
    position: relative;
    font-family: "Arimo", Arial, sans-serif;
  }
  .card {
    position: absolute;
    width: 689px;
    height: 393px;
    overflow: hidden;
  }
  .card-front { left: 266px; top: 158px; background: var(--paper); }
  .card-back { left: 262px; top: 651px; background: var(--brand-blue); }

  .brand-name {
    position: absolute;
    left: 462px; top: 70px;
    width: 181px;
    text-align: center;
    font-weight: 700;
    font-size: 28px;
    line-height: 1.15;
    color: var(--brand-blue);
  }

  .employee-name {
    position: absolute;
    left: 48px; top: 220px;
    font-family: "Cinzel", "Times New Roman", serif;
    font-weight: 700;
    font-size: 27px;
    letter-spacing: 0.5px;
    color: var(--brand-blue);
    white-space: nowrap;
  }
  .employee-title {
    position: absolute;
    left: 48px; top: 252px;
    font-size: 16px;
    color: var(--brand-red);
  }
  .divider {
    position: absolute;
    left: 48px; top: 281px;
    width: 595px; height: 1px;
    background: var(--rule-grey);
  }

  .contact-list {
    position: absolute;
    left: 44px; top: 293px;
    list-style: none;
  }
  .contact-item {
    display: flex;
    align-items: center;
    height: 21px;
    font-size: 16px;
    color: var(--ink-grey);
  }
  .contact-icon {
    width: 14px; height: 14px;
    margin-right: 12px;
    fill: var(--brand-blue);
    flex: none;
  }

  .address {
    position: absolute;
    right: 43px; top: 295px;
    text-align: right;
    font-size: 16px;
    line-height: 21px;
    color: var(--ink-grey);
  }

  .footer-bands {
    position: absolute;
    left: 0; top: 361px;
    width: 689px; height: 32px;
  }
  .website {
    position: absolute;
    right: 41px; top: 367px;
    font-size: 16px;
    color: var(--paper);
  }

  .back-brand {
    position: absolute;
    left: 0; top: 0;
    width: 100%; height: 100%;
    display: flex;
    align-items: center;
    justify-content: center;
    font-weight: 700;
    font-size: 46px;
    color: var(--back-mark);
  }
</style>
</head>
<body>

<section class="card card-front" aria-label="Business card front">
  <div class="brand-name">Kelbrook Forge Co.</div>

  <h1 class="employee-name">TOM PELLING</h1>
  <p class="employee-title">Sales &amp; Estimating</p>
  <div class="divider"></div>

  <ul class="contact-list">
    <li class="contact-item">
      <svg class="contact-icon" viewBox="0 0 24 24" aria-hidden="true"><path d="M6.6 10.8c1.4 2.8 3.8 5.1 6.6 6.6l2.2-2.2c.3-.3.7-.4 1-.2 1.1.4 2.3.6 3.6.6.6 0 1 .4 1 1V20c0 .6-.4 1-1 1C10.6 21 3 13.4 3 4c0-.6.4-1 1-1h3.5c.6 0 1 .4 1 1 0 1.3.2 2.5.6 3.6.1.3 0 .7-.2 1l-2.3 2.2z"/></svg>
      (610) 555-0143
    </li>
    <li class="contact-item">
      <svg class="contact-icon" viewBox="0 0 24 24" aria-hidden="true"><path d="M7 1h10a2 2 0 0 1 2 2v18a2 2 0 0 1-2 2H7a2 2 0 0 1-2-2V3a2 2 0 0 1 2-2zm0 3v14h10V4H7zm5 15.5a1 1 0 1 0 0 2 1 1 0 0 0 0-2z"/></svg>
      (610) 555-0178
    </li>
    <li class="contact-item">
      <svg class="contact-icon" viewBox="0 0 24 24" aria-hidden="true"><path d="M2 6h20v13H2V6zm2 2v.5l8 5.5 8-5.5V8l-8 5.3L4 8z"/></svg>
      info@kelbrookforge.example
    </li>
  </ul>

  <address class="address" style="font-style:normal">
    48 Dunmore Ave Suite 3305<br>
    Trainer, PA 19074
  </address>

  <svg class="footer-bands" viewBox="0 0 689 32" aria-hidden="true">
    <rect x="0" y="20" width="689" height="12" fill="var(--brand-blue)"/>
    <polygon points="0,2 438,2 431,16 0,16" fill="var(--brand-red)"/>
    <polygon points="446,0 689,0 689,32 434,32 434,18 441,18" fill="var(--brand-blue)"/>
  </svg>
  <span class="website">www.kelbrookforge.example</span>
</section>

<section class="card card-back" aria-label="Business card back">
  <div class="back-brand">Kelbrook Forge Co.</div>
</section>

</body>
</html>
```